Redesign of business card for Birchline Mechanical

We are looking for a new design for our business cards for Birchline Mechanical. We are a plumbing & HVAC construction company, operating on the West Coast of Canada and USA. Logo attached.
Industry/Entity Type
Construction - Plumbing & HVAC
Contact Information for Business Card
Name, address, phone numbers, email, website address
Look and feel
Each slider illustrates characteristics of the customer's brand and the style your logo design should communicate.

```html
<!DOCTYPE html>
<html lang="en">
<head>
<meta charset="utf-8">
<title>Birchline Mechanical – Business Card</title>
<link href="https://fonts.googleapis.com/css2?family=Montserrat:wght@700&family=Open+Sans:wght@400;600&display=swap" rel="stylesheet">
<style>
  :root {
    --stage: #6e6f72;
    --card-light: #ffffff;
    --card-dark: #161616;
    --ink: #111111;
    --ink-soft: #555555;
    --ink-muted: #8a8a8a;
    --gloss: #2a2a2a;
  }
  * { margin: 0; padding: 0; box-sizing: border-box; }
  html, body {
    width: 1200px;
    height: 781px;
    overflow: hidden;
  }
  body {
    background: radial-gradient(ellipse at 50% 40%, #8a8b8e 0%, var(--stage) 70%);
    position: relative;
    font-family: "Open Sans", sans-serif;
    color: var(--ink);
  }
  .card {
    position: absolute;
    border-radius: 22px;
    box-shadow: 0 18px 40px rgba(0,0,0,0.35);
  }
  .card-front {
    left: 190px;
    top: 110px;
    width: 330px;
    height: 560px;
    background: var(--card-light);
    padding: 56px 34px 40px;
    display: flex;
    flex-direction: column;
    align-items: center;
    text-align: center;
  }
  .brand {
    display: flex;
    align-items: center;
    gap: 10px;
    font-family: "Open Sans", sans-serif;
    font-weight: 600;
    font-size: 21px;
    color: var(--ink);
    line-height: 1.15;
  }
  .brand-mark {
    width: 26px;
    height: 26px;
    border: 4px solid var(--ink);
    flex-shrink: 0;
  }
  .person {
    margin-top: 64px;
  }
  .person-name {
    font-family: "Montserrat", sans-serif;
    font-weight: 700;
    font-size: 24px;
    color: var(--ink);
  }
  .person-role {
    font-size: 15px;
    color: var(--ink-muted);
    margin-top: 4px;
  }
  .person-rule {
    width: 44px;
    height: 3px;
    background: var(--ink);
    margin: 10px auto 0;
  }
  .address {
    margin-top: 48px;
    font-size: 16px;
    line-height: 1.5;
    color: var(--ink-soft);
  }
  .contact-icons {
    margin-top: 36px;
    display: flex;
    gap: 10px;
    justify-content: center;
  }
  .contact-icons svg {
    width: 14px;
    height: 14px;
    fill: none;
    stroke: var(--ink-muted);
    stroke-width: 1.6;
  }
  .contact-list {
    margin-top: 22px;
    list-style: none;
    font-size: 17px;
    line-height: 1.65;
    letter-spacing: 0.5px;
    color: var(--ink);
  }
  .contact-list .phone { letter-spacing: 3px; }
  .card-back {
    left: 630px;
    top: 240px;
    width: 520px;
    height: 300px;
    background: linear-gradient(135deg, #1d1d1d 0%, var(--card-dark) 60%, #0e0e0e 100%);
    display: flex;
    align-items: center;
    justify-content: center;
  }
  .card-back .brand {
    font-size: 34px;
    color: var(--gloss);
    gap: 16px;
  }
  .card-back .brand-mark {
    width: 40px;
    height: 40px;
    border: 6px solid var(--gloss);
  }
</style>
</head>
<body>
  <section class="card card-front" aria-label="Business card front">
    <div class="brand">
      <span class="brand-mark"></span>
      <span class="brand-name">Birchline Mechanical</span>
    </div>

    <div class="person">
      <p class="person-name">Dale Whitmore</p>
      <p class="person-role">Owner</p>
      <div class="person-rule"></div>
    </div>

    <p class="address">4127 Harbor View Road,<br>Suite 200, Tustin, CA 92780</p>

    <div class="contact-icons" aria-hidden="true">
      <svg viewBox="0 0 16 16"><path d="M4 1.5h2.5l1 3.5-1.8 1.2a8 8 0 0 0 4.1 4.1L11 8.5l3.5 1V12a2 2 0 0 1-2 2A11 11 0 0 1 2 3.5a2 2 0 0 1 2-2z"/></svg>
      <svg viewBox="0 0 16 16"><rect x="1.5" y="3.5" width="13" height="9"/><path d="M1.5 3.5 8 9l6.5-5.5"/></svg>
      <svg viewBox="0 0 16 16"><circle cx="8" cy="8" r="6.5"/><ellipse cx="8" cy="8" rx="2.8" ry="6.5"/><path d="M1.5 8h13"/></svg>
    </div>

    <ul class="contact-list">
      <li class="phone">213-555-0148</li>
      <li class="email">info@birchlinemech.com</li>
      <li class="web">www.birchlinemech.com</li>
    </ul>
  </section>

  <section class="card card-back" aria-label="Business card back">
    <div class="brand">
      <span class="brand-mark"></span>
      <span class="brand-name">Birchline Mechanical</span>
    </div>
  </section>
</body>
</html>
```